PowerPoint design MedoraVix

We need a PowerPoint set-up based upon our existing logo (see joint file)
Our company is operating in the health care and life science sector. We are mainly focussing on international business

Target Market(s)

International

Industry/Entity Type

health care and life sciences

Requirements
Must have
• Logos as added

```html
<!DOCTYPE html>
<html lang="en">
<head>
<meta charset="utf-8">
<title>MedoraVix – Presentation Template</title>
<link href="https://fonts.googleapis.com/css2?family=Montserrat:wght@400;500;600;700&display=swap" rel="stylesheet">
<style>
:root{
  --blue:#0d4c8c;
  --green:#54b948;
  --stage:#e6e6e6;
  --white:#ffffff;
  --ink:#2b2b2b;
  --soft:#ededed;
  --gray:#a6a6a6;
  --gray-dark:#7f7f7f;
}
*{margin:0;padding:0;box-sizing:border-box}
html,body{width:1200px;height:1153px;overflow:hidden;background:var(--stage)}
body{font-family:"Montserrat",Arial,sans-serif;color:var(--ink)}
.canvas{position:relative;width:1200px;height:1153px;background:var(--stage)}
.slide{position:absolute;width:296px;height:167px;background:var(--white);overflow:hidden;box-shadow:0 1px 3px rgba(0,0,0,.18)}
.abs{position:absolute}
.slide-title{position:absolute;left:15px;top:9px;font-size:7.5px;font-weight:700;color:var(--blue);letter-spacing:.1px;line-height:1.1}
.slide-title.light{color:var(--white)}
.caps{font-weight:700;text-transform:uppercase}
.body{font-size:2.6px;line-height:1.35;color:var(--ink)}
.body.light{color:var(--white)}
.brand{position:absolute;right:14px;bottom:6px;display:flex;align-items:center;gap:2px;font-size:3.6px;font-weight:600;color:var(--blue)}
.brand .dot{width:5px;height:5px;border-radius:50%;background:var(--blue)}
.brand.large{font-size:11px;gap:5px}
.brand.large .dot{width:14px;height:14px}
.photo{position:absolute}
.circle{border-radius:50%}
.ph-warm{background:linear-gradient(135deg,#b9a58e,#6f5b48 55%,#3d3a3c)}
.ph-clinic{background:linear-gradient(160deg,#e9eef5,#3b3ca0 50%,#6f86c4)}
.ph-cool{background:linear-gradient(140deg,#eef1f4,#b6c3d0 55%,#7a8b9c)}
.ph-room{background:linear-gradient(150deg,#d9c2a4,#b69874 60%,#8e7d6d)}
.ph-food{background:radial-gradient(circle at 40% 40%,#d74b3a,#e38b2f 35%,#9aa05e 65%,#ddd5c4)}
.ph-light{background:linear-gradient(150deg,#f2f2f2,#d8d5d0 60%,#a7a29b)}
.ph-red{background:linear-gradient(120deg,#e9e7e4,#b8b3ad 40%,#b3272d 70%,#7b6d66)}
.ph-green{background:linear-gradient(150deg,#e2dccd,#a9b38a 50%,#5d7a3b)}
.ph-skin{background:linear-gradient(140deg,#f2ddd2,#e58fae 45%,#7d5a4a)}
.ph-autumn{background:linear-gradient(140deg,#8a7a4b,#c9a066 45%,#6c5a3a)}
.ph-office{background:linear-gradient(160deg,#d9d4cd,#8d857b 55%,#3d3935)}
.ph-blue{background:radial-gradient(circle at 50% 50%,#1e9be0,#0b4f8f 70%)}
.ph-park{background:linear-gradient(150deg,#b9a25a,#5f7a36 50%,#2f3f26)}
.ph-forest{background:linear-gradient(120deg,#c9c2b3,#7f6c56 50%,#3f3429)}
.tick{position:absolute;width:6px;height:6px}
.agenda-list{position:absolute;list-style:none;color:var(--ink)}
.agenda-list li{display:flex;align-items:center;height:7.1px;font-size:3.8px;line-height:1}
.agenda-list b{display:inline-block;width:9px;color:var(--blue);font-weight:700;font-size:3.2px;line-height:1}
.table-row{position:absolute;left:15px;width:166px;height:6px;display:flex;font-size:2.6px;align-items:center}
.table-row span{height:6px;display:flex;align-items:center;padding-left:5px;background:var(--soft)}
.table-row span:first-child{width:91px;margin-right:1px}
.table-row span:last-child{flex:1}
.tier{position:absolute;width:60px}
.tier h4{font-size:3.6px;font-weight:700;color:var(--blue);line-height:1.2}
.tier h5{font-size:3.6px;font-weight:500;color:var(--green);margin-bottom:5px}
.tier .price{font-size:4.8px;font-weight:700;font-style:italic;color:var(--ink);margin-bottom:2px}
.tier ul{font-size:3.1px;line-height:1.45;padding-left:6px}
.team-card{position:absolute;width:72px}
.team-card .head{display:flex;align-items:center;gap:3px;margin-bottom:3px}
.avatar{width:11px;height:11px;border-radius:50%;background:linear-gradient(#c9ccd1,#8a8f96)}
.team-card .name{font-size:2.4px;color:var(--green);line-height:1.3}
.team-card .role{font-size:2.4px;color:var(--blue);font-weight:700}
.milestone{position:absolute;width:50px;text-align:center;font-size:2.4px;line-height:1.3}
.milestone .project{color:var(--green);font-weight:600;font-size:3px;margin-bottom:9px}
.milestone .head{font-weight:700;font-size:3px;margin-bottom:3px}
.year{position:absolute;width:14px;height:14px;border-radius:50%;color:var(--white);font-size:2.4px;display:flex;align-items:center;justify-content:center}
</style>
</head>
<body>
<main class="canvas">

  <!-- Business summary -->
  <section class="slide" style="left:102px;top:62px">
    <div class="photo circle ph-warm" role="img" aria-label="Hands typing on a laptop" style="left:28px;top:18px;width:124px;height:124px"></div>
    <h1 class="slide-title" style="left:192px;top:35px;font-size:9.5px">BUSINESS<br>SUMMARY</h1>
    <div class="abs" style="left:164px;top:69px;width:132px;height:28px;background:var(--blue)"></div>
    <p class="abs caps" style="left:192px;top:73px;width:100px;font-size:4.8px;line-height:1.25;color:var(--white)">Lorem ipsum dolor sit amet, consectetuer adipiscing elit, sed di</p>
    <div class="brand large" style="right:28px;bottom:10px"><span class="dot"></span>MedoraVix</div>
  </section>

  <!-- Methods of differentiation -->
  <section class="slide" style="left:463px;top:62px">
    <div class="abs" style="left:107px;top:40px;width:83px;height:127px;background:var(--soft)"></div>
    <div class="photo circle ph-clinic" role="img" aria-label="Surgeon in scrubs and mask at work" style="left:70px;top:-60px;width:150px;height:150px"></div>
    <div class="abs" style="left:9px;top:0;width:112px;height:30px;background:var(--green);border-radius:0 0 8px 8px"></div>
    <h2 class="slide-title light" style="top:7px;font-size:7px">METHODS OF<br>DIFFERENTIATION</h2>
    <svg class="tick" style="left:50px;top:74px" viewBox="0 0 10 10"><circle cx="5" cy="5" r="5" fill="#54b948"/><path d="M2.8 5.2l1.5 1.5 3-3.2" stroke="#fff" stroke-width="1.2" fill="none"/></svg>
    <svg class="tick" style="left:145px;top:99px" viewBox="0 0 10 10"><circle cx="5" cy="5" r="5" fill="#54b948"/><path d="M2.8 5.2l1.5 1.5 3-3.2" stroke="#fff" stroke-width="1.2" fill="none"/></svg>
    <svg class="tick" style="left:238px;top:74px" viewBox="0 0 10 10"><circle cx="5" cy="5" r="5" fill="#54b948"/><path d="M2.8 5.2l1.5 1.5 3-3.2" stroke="#fff" stroke-width="1.2" fill="none"/></svg>
    <div class="abs" style="left:16px;top:85px;width:74px;text-align:center">
      <p style="font-size:3.4px;color:var(--blue);font-weight:600;margin-bottom:4px">Network of Providers</p>
      <p class="body" style="font-size:3px">Lorem ipsum dolor sit amet, consectetuer adipiscing elit, sed diam nonummy nibh euismod Lorem ipsum dolor sit amet, consectetusmod</p>
    </div>
    <div class="abs" style="left:111px;top:110px;width:74px;text-align:center">
      <p style="font-size:3.4px;color:var(--blue);font-weight:600;margin-bottom:4px">Network of Providers</p>
      <p class="body" style="font-size:3px">Lorem ipsum dolor sit amet, consectetuer adipiscing elit, sed diam nonummy nibh euismod Lorem ipsum dolor sit amet, consectetusmod</p>
    </div>
    <div class="abs" style="left:204px;top:85px;width:74px;text-align:center">
      <p style="font-size:3.4px;color:var(--blue);font-weight:600;margin-bottom:4px">Network of Providers</p>
      <p class="body" style="font-size:3px">Lorem ipsum dolor sit amet, consectetuer adipiscing elit, sed diam nonummy nibh euismod Lorem ipsum dolor sit amet, consectetusmod</p>
    </div>
    <div class="brand"><span class="dot"></span>MedoraVix</div>
  </section>

  <!-- Graphic 01 -->
  <section class="slide" style="left:810px;top:62px">
    <div class="abs" style="left:11px;top:0;width:85px;height:167px;background:var(--blue)"></div>
    <h2 class="slide-title light" style="top:8px">GRAPHIC 01</h2>
    <p class="abs caps" style="left:15px;top:29px;width:68px;font-size:3.6px;line-height:1.2;color:var(--white)">Lorem ipsum dolor sit amet, consectetuer adipiscing elit, sed diam nonummy nibh euismod tincidunt ut laoreet</p>
    <p class="abs body light" style="left:15px;top:69px;width:66px">Lorem ipsum dolor sit amet, consectetuer adipiscing elit, sed diam nonummy nibh euismod tincidunt ut laoreet dolore magna aliquam erat volutpat. Ut wisi enim ad minim veniam, quis nostrud exerci tation ullamcorper suscipit lobortis nisl ut aliquip ex ea commodo consequat. Duis autem vel eum iriure dolor in hendrerit in vulputate velit esse molestie consequat, vel illum dolore eu feugiat nulla facilisis at vero eros et accumsan et iusto odio dignissim qui blandit praesent luptatum zzril delenit augue duis dolore te feugait nulla facilisi.<br><br>Lorem ipsum dolor sit amet, cons ectetuer adipiscing elit, sed diam nonummy nibh euismod tincidunt ut laoreet dolore magna aliquam erat volutpat. Ut wisi enim ad minim veniam, quis nostrud exerci tation ullamcorper suscipit lobortis nisl ut aliquip</p>
    <svg class="abs" style="left:0;top:0" width="296" height="167" viewBox="0 0 296 167" font-family="Montserrat, sans-serif" role="img" aria-label="Bar chart of revenue geo-contribution">
      <text x="178" y="55" font-size="3.6" fill="#555" text-anchor="middle">Revenue Geo-Contribution</text>
      <g font-size="2.2" fill="#555" text-anchor="end">
        <text x="99" y="62">40.00%</text><text x="99" y="73">35.00%</text><text x="99" y="84">30.00%</text><text x="99" y="96">25.00%</text>
        <text x="99" y="107">20.00%</text><text x="99" y="118">15.00%</text><text x="99" y="129">10.00%</text><text x="99" y="140">5.00%</text><text x="99" y="152">0.00%</text>
      </g>
      <line x1="103" y1="151" x2="255" y2="151" stroke="#ccc" stroke-width=".4"/>
      <g fill="#0d4c8c">
        <rect x="123" y="73" width="11" height="78"/><rect x="158" y="78" width="11" height="73"/>
        <rect x="192" y="109" width="11" height="42"/><rect x="227" y="120" width="11" height="31"/>
      </g>
      <g font-size="2.2" fill="#555" text-anchor="middle">
        <text x="128.5" y="71">34.75%</text><text x="163.5" y="76">32.63%</text><text x="197.5" y="107">18.64%</text><text x="232.5" y="118">13.98%</text>
        <text x="128.5" y="156">Emerging Market</text><text x="163.5" y="156">US</text><text x="197.5" y="156">Europe (Incl.WE)</text><text x="232.5" y="156">Established RoW</text>
      </g>
    </svg>
    <div class="brand"><span class="dot"></span>MedoraVix</div>
  </section>

  <!-- Agenda -->
  <section class="slide" style="left:102px;top:261px">
    <h2 class="slide-title">AGENDA</h2>
    <div class="photo circle ph-room" role="img" aria-label="Couple sitting on a yoga mat with a laptop" style="left:20px;top:14px;width:145px;height:145px"></div>
    <ol class="agenda-list" style="left:186px;top:34px">
      <li><b>02</b>VISION</li><li><b>03</b>ABOUT</li><li><b>04</b>OUR TEAM</li><li><b>05</b>SUMMARY</li>
      <li><b>06</b>VISION</li><li><b>07</b>ABOUT</li><li><b>08</b>OUR TEAM</li><li><b>09</b>SUMMARY</li>
      <li><b>10</b>VISION</li><li><b>11</b>ABOUT</li><li><b>12</b>OUR TEAM</li><li><b>13</b>SUMMARY</li>
    </ol>
    <div class="abs" style="left:186px;top:124px;width:96px;border-top:.4px solid #999"></div>
    <p class="abs caps body" style="left:186px;top:127px;width:96px;font-weight:400">Lorem ipsum dolor sit amet, consectetuer adipiscing elit, sed diam nonummy nibh euismod tincidunt ut laoreet dolore magna aliquam erat volutpat. Ut wisi enim ad minim veniam, quis n</p>
    <div class="brand"><span class="dot"></span>MedoraVix</div>
  </section>

  <!-- Images -->
  <section class="slide" style="left:463px;top:261px">
    <h2 class="slide-title">IMAGES</h2>
    <div class="photo circle ph-food" role="img" aria-label="Fresh vegetables and mushrooms" style="left:15px;top:24px;width:72px;height:72px"></div>
    <div class="photo circle ph-cool" role="img" aria-label="Hand writing on a clipboard" style="left:133px;top:4px;width:72px;height:72px"></div>
    <h3 class="abs caps" style="left:213px;top:35px;width:72px;font-size:3.8px;color:var(--blue);line-height:1.2">Lorem ipsum dolor sit amet,</h3>
    <p class="abs body" style="left:213px;top:49px;width:72px">consectetuer adipiscing elit, sed diam nonummy nibh euismod tincidunt ut laoreet dolore magna aliquam erat volutpat. Ut wisi enim ad minim veniam, quis nostrud exerci tation ullamcorper suscipit lobortis nisl ut aliquip ex ea commodo consequat. Duis autem</p>
    <h3 class="abs caps" style="left:15px;top:104px;width:72px;font-size:3.8px;color:var(--blue);line-height:1.2">Lorem ipsum dolor sit amet,</h3>
    <p class="abs body" style="left:15px;top:118px;width:68px">consectetuer adipiscing elit, sed diam nonummy nibh euismod tincidunt ut laoreet dolore magna aliquam erat volutpat. Ut wisi enim ad minim veniam, quis nostrud exerci tation ullamcorper suscipit lobortis nisl ut aliquip ex ea commodo consequat. Duis autem</p>
    <div class="abs" style="left:100px;top:83px;width:160px;height:84px;background:var(--green)"></div>
    <div class="photo circle ph-light" role="img" aria-label="Woman stretching her arms overhead" style="left:108px;top:89px;width:72px;height:72px;border:2px solid var(--white)"></div>
    <h3 class="abs caps" style="left:188px;top:118px;width:68px;font-size:3.8px;color:var(--white);line-height:1.2">Lorem ipsum dolor sit amet,</h3>
    <p class="abs body light" style="left:188px;top:132px;width:66px">consectetuer adipiscing elit, sed diam nonummy nibh euismod tincidunt ut laoreet dolore magna aliquam erat volutpat. Ut wisi enim ad minim veniam, quis nostrud exerci tation ullamcorper suscipit lobortis nisl ut aliquip ex ea commodo consequat. Duis autem</p>
    <div class="brand"><span class="dot"></span>MedoraVix</div>
  </section>

  <!-- Our team -->
  <section class="slide" style="left:810px;top:261px">
    <h2 class="slide-title">OUR TEAM</h2>
    <div class="abs" style="left:172px;top:0;width:124px;height:167px;background:var(--soft)"></div>
    <div class="photo ph-cool" role="img" aria-label="Doctor in a white coat holding a stethoscope" style="left:178px;top:14px;width:118px;height:153px;border-radius:40px 0 0 0"></div>
    <article class="team-card" style="left:15px;top:23px">
      <div class="head"><span class="avatar"></span><div><p class="name">ALAN PETROSKY</p><p class="role">DIRECTOR</p></div></div>
      <p class="body">Lorem ipsum dolor sit amet, consectetuer adipiscing elit, sed diam nonummy nibh euismod tincidunt ut laoreet dolore magna aliquam erat volutpat. Ut wisi enim ad minim veniam, quis nostrud exerci tation ullamcorper suscipit lobortis nisl ut aliquip ex ea commodo consequat. Duis autem vel eum iriure dolor in hendrerit in vulputate velit esse molestie consequat, vel illum dolore eu feugiat nulla facilisis at vero eros et accumsan et iusto odio dignissim qui blandit praesent luptatum zz</p>
    </article>
    <article class="team-card" style="left:97px;top:23px">
      <div class="head"><span class="avatar"></span><div><p class="name">ALAN PETROSKY</p><p class="role">DIRECTOR</p></div></div>
      <p class="body">Lorem ipsum dolor sit amet, consectetuer adipiscing elit, sed diam nonummy nibh euismod tincidunt ut laoreet dolore magna aliquam erat volutpat. Ut wisi enim ad minim veniam, quis nostrud exerci tation ullamcorper suscipit lobortis nisl ut aliquip ex ea commodo consequat. Duis autem vel eum iriure dolor in hendrerit in vulputate velit esse molestie consequat, vel illum dolore eu feugiat nulla facilisis at vero eros et accumsan et iusto odio dignissim qui blandit praesent luptatum zz</p>
    </article>
    <article class="team-card" style="left:15px;top:97px">
      <div class="head"><span class="avatar"></span><div><p class="name">ALAN PETROSKY</p><p class="role">DIRECTOR</p></div></div>
      <p class="body">Lorem ipsum dolor sit amet, consectetuer adipiscing elit, sed diam nonummy nibh euismod tincidunt ut laoreet dolore magna aliquam erat volutpat. Ut wisi enim ad minim veniam, quis nostrud exerci tation ullamcorper suscipit lobortis nisl ut aliquip ex ea commodo consequat. Duis autem vel eum iriure dolor in hendrerit in vulputate velit esse molestie consequat, vel illum dolore eu feugiat nulla facilisis at vero eros et accumsan et iusto odio dignissim qui blandit praesent luptatum zz</p>
    </article>
    <article class="team-card" style="left:97px;top:97px">
      <div class="head"><span class="avatar"></span><div><p class="name">ALAN PETROSKY</p><p class="role">DIRECTOR</p></div></div>
      <p class="body">Lorem ipsum dolor sit amet, consectetuer adipiscing elit, sed diam nonummy nibh euismod tincidunt ut laoreet dolore magna aliquam erat volutpat. Ut wisi enim ad minim veniam, quis nostrud exerci tation ullamcorper suscipit lobortis nisl ut aliquip ex ea commodo consequat. Duis autem vel eum iriure dolor in hendrerit in vulputate velit esse molestie consequat, vel illum dolore eu feugiat nulla facilisis at vero eros et accumsan et iusto odio dignissim qui blandit praesent luptatum zz</p>
    </article>
    <div class="brand" style="background:var(--white);padding:1px 3px"><span class="dot"></span>MedoraVix</div>
  </section>

  <!-- Checkmark -->
  <section class="slide" style="left:102px;top:465px">
    <h2 class="slide-title">CHECKMARK</h2>
    <p class="abs body" style="left:15px;top:18px;width:96px">Lorem ipsum dolor sit amet, consectetuer adipiscing elit, sed diam nonummy nibh euismod tincidunt ut laoreet dolore magna aliquam erat volutpat. Ut wisi enim ad minim veniam, quis nostrud exerci tation ullamcorper suscipit lobortis nisl ut aliquip ex ea commodo consequat. Duis autem vel eum iriure dolor in hendrerit in vulputate velit esse molestie consequat, vel illum dolore eu feugiat nulla facilisis at vero eros et accumsan et iusto odio dignissim qui blandit praesent luptatum zzril delenit augue duis dolore te feugait nulla facilisi.<br><br>Lorem ipsum dolor sit amet, cons ectetuer adipiscing elit, sed diam nonummy nibh euismod tincidunt ut laoreet dolore magna aliquam erat vol</p>
    <div class="photo ph-light" role="img" aria-label="Nurse in a white uniform with a stethoscope" style="left:115px;top:0;width:163px;height:80px"></div>
    <div class="abs" style="left:0;top:80px;width:296px;height:67px;background:var(--blue);clip-path:polygon(0 0,100% 0,100% 31%,220px 100%,0 100%)"></div>
    <div class="abs" style="left:15px;top:87px;width:260px;display:flex;gap:7px">
      <div style="width:36px"><svg width="5" height="5" viewBox="0 0 10 10"><circle cx="5" cy="5" r="5" fill="#54b948"/><path d="M2.8 5.2l1.5 1.5 3-3.2" stroke="#fff" stroke-width="1.2" fill="none"/></svg><p class="body light" style="font-size:2.9px">To protect customers' digital experiences &amp; secure their privacy. To protect customers' digital experiences &amp; secure their privacy.</p></div>
      <div style="width:36px"><svg width="5" height="5" viewBox="0 0 10 10"><circle cx="5" cy="5" r="5" fill="#54b948"/><path d="M2.8 5.2l1.5 1.5 3-3.2" stroke="#fff" stroke-width="1.2" fill="none"/></svg><p class="body light" style="font-size:2.9px">To protect customers' digital experiences &amp; secure their privacy. To protect customers' digital experiences &amp; secure their privacy.</p></div>
      <div style="width:36px"><svg width="5" height="5" viewBox="0 0 10 10"><circle cx="5" cy="5" r="5" fill="#54b948"/><path d="M2.8 5.2l1.5 1.5 3-3.2" stroke="#fff" stroke-width="1.2" fill="none"/></svg><p class="body light" style="font-size:2.9px">To protect customers' digital experiences &amp; secure their privacy. To protect customers' digital experiences &amp; secure their privacy.</p></div>
      <div style="width:36px"><svg width="5" height="5" viewBox="0 0 10 10"><circle cx="5" cy="5" r="5" fill="#54b948"/><path d="M2.8 5.2l1.5 1.5 3-3.2" stroke="#fff" stroke-width="1.2" fill="none"/></svg><p class="body light" style="font-size:2.9px">To protect customers' digital experiences &amp; secure their privacy. To protect customers' digital experiences &amp; secure their privacy.</p></div>
      <div style="width:36px"><svg width="5" height="5" viewBox="0 0 10 10"><circle cx="5" cy="5" r="5" fill="#54b948"/><path d="M2.8 5.2l1.5 1.5 3-3.2" stroke="#fff" stroke-width="1.2" fill="none"/></svg><p class="body light" style="font-size:2.9px">To protect customers' digital experiences &amp; secure their privacy. To protect customers' digital experiences &amp; secure their privacy.</p></div>
      <div style="width:36px"><svg width="5" height="5" viewBox="0 0 10 10"><circle cx="5" cy="5" r="5" fill="#54b948"/><path d="M2.8 5.2l1.5 1.5 3-3.2" stroke="#fff" stroke-width="1.2" fill="none"/></svg><p class="body light" style="font-size:2.9px">To protect customers' digital experiences &amp; secure their privacy. To protect customers' digital experiences &amp; secure their privacy.</p></div>
    </div>
    <div class="brand"><span class="dot"></span>MedoraVix</div>
  </section>

  <!-- Table -->
  <section class="slide" style="left:463px;top:465px">
    <h2 class="slide-title">TABLE</h2>
    <p class="abs body" style="left:15px;top:25px;width:165px">Lorem ipsum dolor sit amet, consectetuer adipiscing elit, sed diam nonummy nibh euismod tincidunt ut laoreet dolore magna aliquam erat volutpat. Ut wisi enim ad minim veniam, quis nostrud exerci tation ullamcorper suscipit lobortis nisl ut aliquip ex ea commodo consequat. Duis autem vel eum iriure dolor in hendrerit in vulputate velit esse molestie consequat, vel illum dolore eu feugiat nulla facilisis at vero eros et accumsan et iusto odio dignissim qui blandit praesent luptatum zzril delenit augue duis dolore te feugait nulla facilisi. Lorem ipsum dolor sit amet, cons ectetuer adipiscing elit, sed dia<br><br>m nonummy nibh euismod tincidunt ut laoreet dolore magna aliquam erat volutpat. Ut wisi enim ad minim veniam, quis nostrud exerci tation ullamcorper suscipit lobortis nisl ut aliquip ex ea commodo consequat. Lorem ipsum dolor sit amet, consectetuer adipiscing elit, sed diam nonummy nibh euismod tincidunt ut laoreet dolore magna aliquam erat volutpat. Ut wisi enim ad minim veniam, quis nostrud exerci tation ullam</p>
    <div class="table-row" style="top:78px;height:5px;font-weight:700;color:var(--white)"><span style="background:var(--blue);height:5px">BASE</span><span style="background:var(--green);height:5px">SCORE</span></div>
    <div class="table-row" style="top:84px"><span>AVERAGE MONTHLY QUOTES</span><span>432</span></div>
    <div class="table-row" style="top:93px"><span>AVERAGE MONTHLY QUOTES</span><span>946</span></div>
    <div class="table-row" style="top:102px"><span>AVERAGE MONTHLY QUOTES</span><span>350</span></div>
    <div class="table-row" style="top:111px"><span>AVERAGE MONTHLY QUOTES</span><span>432</span></div>
    <div class="table-row" style="top:120px"><span>AVERAGE MONTHLY QUOTES</span><span>946</span></div>
    <div class="table-row" style="top:128px"><span>AVERAGE MONTHLY QUOTES</span><span>350</span></div>
    <div class="table-row" style="top:137px"><span>AVERAGE MONTHLY QUOTES</span><span>946</span></div>
    <div class="table-row" style="top:146px"><span>AVERAGE MONTHLY QUOTES</span><span>350</span></div>
    <div class="photo ph-red" role="img" aria-label="Doctor holding a red stethoscope" style="left:186px;top:0;width:110px;height:167px"></div>
    <div class="brand" style="background:var(--white);padding:1px 3px"><span class="dot"></span>MedoraVix</div>
  </section>

  <!-- Pricing -->
  <section class="slide" style="left:810px;top:465px">
    <div class="photo ph-green" role="img" aria-label="Letter tiles spelling healthcare beside green leaves" style="left:0;top:0;width:296px;height:98px;clip-path:polygon(0 0,100% 0,100% 26%,0 100%)"></div>
    <h2 class="slide-title light">PRICING</h2>
    <div class="abs" style="left:0;top:21px;width:118px;height:30px;background:var(--green);opacity:.92;border-radius:0 0 8px 0"></div>
    <p class="abs body light" style="left:15px;top:24px;width:98px;font-size:2.8px">Lorem ipsum dolor sit amet, consectetuer adipiscing elit, sed diam nonummy nibh euismod tincidunt ut laoreet dolore magna aliquam erat volutpat. Ut wisi enim ad minim veniam, quis nostrud exerci tation ullamcorper suscipit lobortis nisl ut aliquip ex ea commodo consequat. Duis autem vel eum iriure dolor</p>
    <div class="abs" style="left:79px;top:83px;width:.4px;height:45px;background:#999"></div>
    <div class="abs" style="left:147px;top:67px;width:.4px;height:45px;background:#999"></div>
    <div class="abs" style="left:215px;top:50px;width:.4px;height:45px;background:#999"></div>
    <div class="tier" style="left:17px;top:101px"><h4>MOST DIFFICULT</h4><h5>ENTRY LEVEL</h5><p class="price">$3690</p><ul><li>Small meetings</li><li>Small meetings</li><li>Small meetings</li><li>Small meetings</li></ul></div>
    <div class="tier" style="left:84px;top:84px"><h4>DIFFICULT</h4><h5>MID-LEVEL</h5><p class="price">$4290</p><ul><li>Small meetings</li><li>Small meetings</li><li>Small meetings</li><li>Small meetings</li></ul></div>
    <div class="tier" style="left:152px;top:68px"><h4>EASIER</h4><h5>ADVANCED</h5><p class="price">$4890</p><ul><li>Small meetings</li><li>Small meetings</li><li>Small meetings</li><li>Small meetings</li></ul></div>
    <div class="tier" style="left:220px;top:49px"><h4>EASIEST</h4><h5>PREMIUM</h5><p class="price">$5490</p><ul><li>Small meetings</li><li>Small meetings</li><li>Small meetings</li><li>Small meetings</li></ul></div>
    <div class="brand"><span class="dot"></span>MedoraVix</div>
  </section>

  <!-- Graphic 03 -->
  <section class="slide" style="left:102px;top:689px">
    <h2 class="slide-title">GRAPHIC 03</h2>
    <svg class="abs" style="left:0;top:0" width="190" height="120" viewBox="0 0 190 120" font-family="Montserrat, sans-serif" role="img" aria-label="Two pie charts of quarterly sales">
      <g font-size="3" fill="#555" text-anchor="middle"><text x="45" y="36">Sales</text><text x="138" y="36">Sales</text></g>
      <g transform="translate(45 71) scale(1.25)">
        <path d="M0 0L0-24A24 24 0 1 1-15.4 18.4Z" fill="#a6a6a6"/><path d="M0 0L-15.4 18.4A24 24 0 0 1-20.8-12Z" fill="#7f7f7f"/>
        <path d="M0 0L-20.8-12A24 24 0 0 1-10.1-21.8Z" fill="#0d4c8c"/><path d="M0 0L-10.1-21.8A24 24 0 0 1 0-24Z" fill="#54b948"/>
      </g>
      <g transform="translate(138 71) scale(1.25)">
        <path d="M0 0L0-24A24 24 0 1 1-15.4 18.4Z" fill="#a6a6a6"/><path d="M0 0L-15.4 18.4A24 24 0 0 1-20.8-12Z" fill="#7f7f7f"/>
        <path d="M0 0L-20.8-12A24 24 0 0 1-10.1-21.8Z" fill="#0d4c8c"/><path d="M0 0L-10.1-21.8A24 24 0 0 1 0-24Z" fill="#54b948"/>
      </g>
      <g font-size="2" fill="#777">
        <circle cx="17" cy="107" r=".8" fill="#a6a6a6"/><text x="19" y="107.7">1st Qtr</text><circle cx="28" cy="107" r=".8" fill="#7f7f7f"/><text x="30" y="107.7">2nd Qtr</text>
        <circle cx="40" cy="107" r=".8" fill="#0d4c8c"/><text x="42" y="107.7">3rd Qtr</text><circle cx="51" cy="107" r=".8" fill="#e3b23c"/><text x="53" y="107.7">4th Qtr</text>
        <circle cx="110" cy="107" r=".8" fill="#a6a6a6"/><text x="112" y="107.7">1st Qtr</text><circle cx="121" cy="107" r=".8" fill="#7f7f7f"/><text x="123" y="107.7">2nd Qtr</text>
        <circle cx="133" cy="107" r=".8" fill="#0d4c8c"/><text x="135" y="107.7">3rd Qtr</text><circle cx="144" cy="107" r=".8" fill="#e3b23c"/><text x="146" y="107.7">4th Qtr</text>
      </g>
    </svg>
    <p class="abs body" style="left:15px;top:123px;width:76px;font-size:3px">Lorem ipsum dolor sit amet, consectetuer adipiscing elit, sed diam nonummy nibh euismod tincidunt ut laoreet dolore magna aliquam erat volutpat. Ut wisi enim ad minim veniam, quis nostrud exerci tation ullamcorper suscipit lobortis nisl ut aliquip ex ea commodo consequat. Duis autem vel</p>
    <p class="abs body" style="left:111px;top:123px;width:76px;font-size:3px">Lorem ipsum dolor sit amet, consectetuer adipiscing elit, sed diam nonummy nibh euismod tincidunt ut laoreet dolore magna aliquam erat volutpat. Ut wisi enim ad minim veniam, quis nostrud exerci tation ullamcorper suscipit lobortis nisl ut aliquip ex ea commodo consequat. Duis autem vel</p>
    <div class="photo ph-skin" role="img" aria-label="Hands applying pink kinesiology tape to a shoulder" style="left:192px;top:0;width:104px;height:167px"></div>
    <div class="brand" style="background:var(--white);padding:1px 3px"><span class="dot"></span>MedoraVix</div>
  </section>

  <!-- About us 2 -->
  <section class="slide" style="left:463px;top:689px">
    <div class="photo ph-autumn" role="img" aria-label="Smiling woman outdoors among autumn leaves" style="left:0;top:0;width:296px;height:100px;clip-path:path('M0 0H240C280 0 283 70 255 88C248 93 240 92 230 88L10 48H0Z')"></div>
    <h2 class="slide-title light">ABOUT US 2</h2>
    <div class="abs" style="left:10px;top:48px;width:75px;height:119px;background:var(--green);clip-path:polygon(0 0,100% 17%,100% 100%,0 100%)"></div>
    <p class="abs caps" style="left:15px;top:101px;width:68px;font-size:3.8px;line-height:1.2;color:var(--white)">Lorem ipsum dolor sit amet, consectetuer adipiscing elit, sed diam nonummy nibh euismod tincidunt ut laoreet</p>
    <p class="abs body" style="left:91px;top:100px;width:88px">Lorem ipsum dolor sit amet, consectetuer adipiscing elit, sed diam nonummy nibh euismod tincidunt ut laoreet dolore magna aliquam erat volutpat. Ut wisi enim ad minim veniam, quis nostrud exerci tation ullamcorper suscipit lobortis nisl ut aliquip ex ea commodo consequat. Duis autem vel eum iriure dolor in hendrerit in vulputate velit esse molestie consequat, vel illum dolore eu feugiat nulla facilisis at vero eros et accumsan et iusto odio dignissim qui blandit praesent luptatum zzril delenit augue duis dolore te feugait nulla facilisi.<br><br>Lorem ipsum dolor sit amet, cons ectetuer adipiscing elit, sed diam nonummy nibh euismod tincidunt ut laoreet dolore magna aliquam erat volutpat. Ut wisi enim ad minim veniam, quis nostrud exerci tation ullamcorper</p>
    <div class="brand"><span class="dot"></span>MedoraVix</div>
  </section>

  <!-- Graphic 02 -->
  <section class="slide" style="left:810px;top:689px">
    <div class="photo ph-office" role="img" aria-label="Man reading a book at an office desk" style="left:0;top:0;width:296px;height:78px"></div>
    <h2 class="slide-title light">GRAPHIC 02</h2>
    <div class="abs" style="left:34px;top:77.5px;width:222px;height:1px;background:var(--white)"></div>
    <span class="year" style="left:34px;top:71px;background:var(--green)">2014</span>
    <span class="year" style="left:86px;top:71px;background:var(--green)">2015</span>
    <span class="year" style="left:138px;top:71px;background:var(--green)">2016</span>
    <span class="year" style="left:190px;top:71px;background:var(--blue)">2017</span>
    <span class="year" style="left:242px;top:71px;background:var(--green)">2018</span>
    <div class="milestone" style="left:16px;top:95px"><p class="project">Project One</p><p class="head">Marketers</p><p>To be successful, marketers should understand the life cycle of a product</p></div>
    <div class="milestone" style="left:68px;top:95px"><p class="project">Project Two</p><p class="head">Marketers</p><p>To be successful, marketers should understand the life cycle of a product</p></div>
    <div class="milestone" style="left:120px;top:95px"><p class="project">Project Tree</p><p class="head">Marketers</p><p>To be successful, marketers should understand the life cycle of a product</p></div>
    <div class="milestone" style="left:172px;top:95px"><p class="project">Project Four</p><p class="head">Marketers</p><p>To be successful, marketers should understand the life cycle of a product</p></div>
    <div class="milestone" style="left:224px;top:95px"><p class="project">Project Five</p><p class="head">Marketers</p><p>To be successful, marketers should understand the life cycle of a product</p></div>
    <div class="brand"><span class="dot"></span>MedoraVix</div>
  </section>

  <!-- About us -->
  <section class="slide" style="left:102px;top:904px">
    <h2 class="slide-title">ABOUT US</h2>
    <p class="abs caps" style="left:15px;top:35px;width:70px;font-size:3.8px;line-height:1.2;color:var(--green)">Lorem ipsum dolor sit amet, consectetuer adipiscing elit, sed diam nonummy nibh euismod tincidunt ut laoreet</p>
    <p class="abs body" style="left:15px;top:84px;width:56px">Lorem ipsum dolor sit amet, consectetuer adipiscing elit, sed diam nonummy nibh euismod tincidunt ut laoreet dolore magna aliquam erat volutpat. Ut wisi enim ad minim veniam, quis nostrud exerci tation ullamcorper suscipit lobortis nisl ut aliquip ex ea commodo consequat. Duis autem vel eum iriure dolor in hendrerit in vulputate velit esse molestie consequat, vel illum dolore eu feugiat nulla facilisis at vero eros et accumsan et iusto odio dignissim qui blandit praesent luptatum zzril</p>
    <p class="abs body" style="left:77px;top:84px;width:56px">Lorem ipsum dolor sit amet, consectetuer adipiscing elit, sed diam nonummy nibh euismod tincidunt ut laoreet dolore magna aliquam erat volutpat. Ut wisi enim ad minim veniam, quis nostrud exerci tation ullamcorper suscipit lobortis nisl ut aliquip ex ea commodo consequat. Duis autem vel eum iriure dolor in hendrerit in vulputate velit esse molestie consequat, vel illum dolore eu feugiat nulla facilisis at vero eros et accumsan et iusto odio dignissim qui blandit praesent luptatum zzril</p>
    <div class="photo circle ph-blue" role="img" aria-label="Hands wearing a fitness watch" style="left:150px;top:22px;width:122px;height:122px"></div>
    <div class="brand"><span class="dot"></span>MedoraVix</div>
  </section>

  <!-- Benefits -->
  <section class="slide" style="left:463px;top:904px">
    <div class="photo ph-park" role="img" aria-label="Woman jogging in a sunny park" style="left:0;top:0;width:140px;height:167px;clip-path:path('M0 0H112C138 45 140 120 88 167H0Z')"></div>
    <h2 class="slide-title light">BENEFITS</h2>
    <svg class="abs" style="left:0;top:0" width="140" height="167" viewBox="0 0 140 167" font-family="Montserrat, sans-serif" role="img" aria-label="Total benefits: 1296">
      <circle cx="55" cy="98" r="34" fill="#0d4c8c" opacity=".92"/>
      <circle cx="103" cy="97" r="24" fill="#54b948" opacity=".85"/>
      <text x="54" y="96" font-size="4.4" fill="#fff" text-anchor="middle">TOTAL</text>
      <text x="54" y="102" font-size="4.4" fill="#fff" text-anchor="middle">BENEFITS</text>
      <text x="103" y="99" font-size="5" font-weight="600" fill="#fff" text-anchor="middle">1296</text>
    </svg>
    <p class="abs caps body" style="left:134px;top:20px;width:136px;font-size:2.9px;font-weight:400">Veniam, quis nostrud exerci tation ullamcorper suscipit lobortis nisl ut aliquip ex ea commodo veniam, quis nostrud exerci tation ullamcorper suscipit lup ex ea commodo veniam, quis nostrud exerci tation ullamcorper suscipit lobortis nisl ut aliquip ex ea commodo veniam, quis nostrud exerci tation ullamcorper suscipit lobortis nisl ut aliquip ex ea com</p>
    <h3 class="abs" style="left:134px;top:66px;font-size:4.6px;color:var(--green);font-weight:600">BENEFITS</h3>
    <ul class="abs body" style="left:134px;top:76px;width:136px;font-size:2.9px;list-style:none">
      <li style="margin-bottom:5px">•&nbsp; Lorem ipsum dolor sit amet, consectetuer adipiscing elit, sed diam nonummy nibh euismod t</li>
      <li style="margin-bottom:5px">•&nbsp; incidunt ut laoreet dolore magna aliquam e</li>
      <li style="margin-bottom:5px">•&nbsp; rat volutpat. Ut wisi enim ad minim veniam, quis nostrud exerci tation ullamcorper suscipit lobortis nisl ut aliquip ex ea commodo veniam, quis nostrud exerci tation ullamcorper suscipit lo</li>
      <li>•&nbsp; bortis nisl ut aliquip ex ea commodo veniam, quis nostrud exerci tation ullamcorper suscipit lobortis nisl ut aliquip ex ea commodo</li>
    </ul>
    <div class="brand"><span class="dot"></span>MedoraVix</div>
  </section>

  <!-- Thank you -->
  <section class="slide" style="left:810px;top:904px">
    <div class="photo ph-forest" role="img" aria-label="Outstretched hand against a blurred forest" style="left:0;top:0;width:296px;height:167px"></div>
    <div class="abs" style="left:0;top:0;width:130px;height:140px;background:var(--white);clip-path:path('M0 0H112C108 60 120 110 96 128C82 138 40 138 0 138Z')"></div>
    <h1 class="abs" style="left:24px;top:40px;font-size:9px;font-weight:700;color:var(--blue)">THANK YOU !</h1>
    <p class="abs" style="left:24px;top:60px;font-size:5.2px;line-height:1.6;font-weight:600;color:var(--ink)">+000 000 000<br>WWW.MEDORAVIX-DEMO.COM<br>INFO@MEDORAVIX-DEMO.COM</p>
    <div class="brand large" style="left:22px;right:auto;bottom:auto;top:94px"><span class="dot"></span>MedoraVix</div>
  </section>

</main>
</body>
</html>
```